Folded Business Cards, Envelopes, Information card and Thank You card.
Gala Tent Company
Folded Business Cards, Envelopes, Information card and Thank You card. - Events
Creative Brief
Modern
Marisol Fenwick-Dutra
Owner-Linen Specialist
2718 Harbor Crest Ave Suite 204B Long Beach CA 90807
marisol@larkspurdrapery.example
larkspurdraperys.example
Our colors are silver, grey, dark plum and eggplant. I would like something modern with maybe translucent floral scrolls in the background. I am open to card back ground color. It can be silver, plum/eggplant or even white. We are a high-end wedding linen rental company. Our clients are mostly female, mid income and are planning a wedding. I am looking for the following items: 1. Business Card. 2. Envelope. 3. Information Card. 4. Thank You Card. Information Card: This is an information card that will be sent out with each order. It will be printed on a 6" x 9" post card one sided. Bellow is the text that will go on the card Important Information Regarding Your Linen Returns. Thank you for allowing Larkspur Drapery linens to share in your special day. To ensure prompt return of your linens, please follow the steps bellow. 1. Please place all linens in the included return duffel bags or the box they arrived in. It returning in a box, please fold linens so that they all fit in the box. Please shake any loose food from linens and insure linens are dry prior to placing in box and bags. NEVER place wet linens in bags, boxes of plastic. If your linens are wet or damp please allow them to air dry prior to packing. If your shipment included chair sashes, please remember to untie each sash prior to return. You account will be billed a fee of $.25 for each sash returned that is untied. 2. If you would like to schedule a ParcelWing pickup, please contact ParcelWing the day PRIOR to your scheduled return date as ParcelWing does not do same pickup. Please note, ParcelWing charges a pickup fee of $8. This fee is paid directly to ParcelWing. You can contact ParcelWing at 1.800.Go.Wing (555-0148). You may also return your linens for free of charge by dropping of your linens at any ParcelWing or ParcelWing Copyhub. Please use the attached pre-paid ParcelWing air-bil that came with your shipment. Lost ParcelWing Air-Bills: Please treat your ParcelWing return air-bills as cash. If they are lost or damaged, please contact us as soon as possible for replacements. We charge a fee of $25 for each lost or damaged air-bill that needs to be replaced. Alternate Shipping Carriers: Your linen rental includes pre-paid return shipping via ParcelWing and include tracking for our warehouse. Please do not return linens using any other shipping provider or any other class of shipping (i.e. Express, Next Day, Over Night these services will be billed back to your account). Late Returns: Our customers depend on your timely return. Please insure our items are dropped off or picked up by ParcelWing the following business day after your event. Items shipped back after the due date are considered late and will be charge a rental fee equal to 50% of your original rental rate prior to any discounts or promotions. Should you have any questions regarding your order please contact our office at 562.555.0173 should you need to reach us after hours or on weekends please leave a message or send an e-mail to afterhours@larkspurdraperys.example. Thank you card: Please also design a matching thank you card that will be printed on a 4" x 6" one sided post card.
Notes: We are using a folded business card: We would like it laid out as follows: Front: Logo with contact details Inside: The inside will have a space where we can glue on a fabric swatch. We would like the swatch to be placed placed in a decorative rectangle that should take up most of the inside. There also needs to be wording under the square that says "Raspberry Satin Back Shantung" we would like this centered. Back: On the back of the card we would like: twitter icon with our twitter id:larkspurcloth youtube logo with our id: larkspurdraperys

```html
<!DOCTYPE html>
<html lang="en">
<head>
<meta charset="utf-8">
<title>Linen Returns Information Card</title>
<link href="https://fonts.googleapis.com/css2?family=Open+Sans:wght@300;400;600;700&display=swap" rel="stylesheet">
<style>
  :root {
    --backdrop: #dcdad6;
    --card: #ffffff;
    --ink: #5a5a5c;
    --ink-soft: #7a7a7d;
    --heading: #6b6b6e;
    --rule: #c9c9cc;
    --band: #e7e7e8;
    --accent: #4a2c45;
  }
  * { box-sizing: border-box; margin: 0; padding: 0; }
  html, body { width: 1200px; height: 768px; overflow: hidden; }
  body {
    background: var(--backdrop);
    font-family: "Open Sans", Arial, sans-serif;
    color: var(--ink);
    position: relative;
  }
  .info-card {
    position: absolute;
    left: 80px; top: 54px;
    width: 1040px; height: 660px;
    background: var(--card);
    box-shadow: 0 2px 10px rgba(0,0,0,0.15);
  }
  .brand {
    position: absolute;
    left: 36px; top: 44px;
    width: 220px;
    text-align: center;
  }
  .brand-square {
    width: 46px; height: 46px;
    margin: 0 auto 16px;
    background: var(--band);
  }
  .brand-name {
    font-size: 22px;
    font-weight: 300;
    letter-spacing: 3px;
    color: var(--ink-soft);
    text-transform: uppercase;
    line-height: 1.3;
  }
  .top-rule {
    position: absolute;
    left: 300px; right: 36px; top: 70px;
    border-top: 1px solid var(--rule);
  }
  .title {
    position: absolute;
    right: 36px; top: 92px;
    text-align: right;
    font-size: 30px;
    font-weight: 400;
    line-height: 1.22;
    color: var(--heading);
  }
  .intro {
    position: absolute;
    left: 72px; top: 198px;
    width: 620px;
    font-size: 14px;
    line-height: 1.45;
    color: var(--ink-soft);
  }
  .steps {
    position: absolute;
    left: 72px; right: 72px; top: 262px;
    display: flex;
    gap: 50px;
  }
  .step {
    flex: 1;
    font-size: 10.6px;
    line-height: 1.42;
    text-align: justify;
  }
  .notes-band {
    position: absolute;
    left: 0; right: 0; top: 458px;
    height: 124px;
    background: var(--band);
    display: flex;
    gap: 36px;
    padding: 16px 72px 0;
  }
  .note {
    flex: 1;
    font-size: 9.4px;
    line-height: 1.38;
  }
  .note-title {
    display: block;
    font-weight: 700;
    color: var(--accent);
  }
  .closing {
    position: absolute;
    left: 60px; right: 60px; top: 598px;
    text-align: center;
    font-size: 12px;
    line-height: 1.5;
  }
  .closing strong { font-weight: 700; color: var(--accent); }
</style>
</head>
<body>
  <main class="info-card">
    <div class="brand">
      <div class="brand-square"></div>
      <div class="brand-name">Larkspur Drapery</div>
    </div>

    <div class="top-rule"></div>
    <h1 class="title">Important Information Regarding<br>Your Linen Returns.</h1>

    <p class="intro">Thank you for allowing Larkspur Drapery linens to share in your special day.<br>To ensure prompt return of your linens, please follow the steps bellow.</p>

    <section class="steps">
      <p class="step">1. Please place all linens in the included return duffel bags or the box they arrived in. It returning in a box, please fold linens so that they all fit in the box. Please shake any loose food from linens and insure linens are dry prior to placing in box and bags. NEVER place wet linens in bags, boxes of plastic. If your linens are wet or damp please allow them to air dry prior to packing. If your shipment included chair sashes, please remember to untie each sash prior to return. You account will be billed a fee of $.25 for each sash returned that is untied.</p>
      <p class="step">2. If you would like to schedule a ParcelWing pickup, please contact ParcelWing the day PRIOR to your scheduled return date as ParcelWing does not do same pickup. Please note, ParcelWing charges a pickup fee of $8. This fee is paid directly to ParcelWing. You can contact ParcelWing at 1.800.Go.Wing (555-0148). You may also return your linens for free of charge by dropping of your linens at any ParcelWing or ParcelWing Copyhub. Please use the attached pre-paid ParcelWing air-bil that came with your shipment.</p>
    </section>

    <section class="notes-band">
      <p class="note"><span class="note-title">Lost ParcelWing Air-Bills:</span>Please treat your ParcelWing return air-bills as cash. If they are lost or damaged, please contact us as soon as possible for replacements. We charge a fee of $25 for each lost or damaged air-bill that needs to be replaced.</p>
      <p class="note"><span class="note-title">Alternate Shipping Carriers:</span>Your linen rental includes pre-paid return shipping via ParcelWing and include tracking for our warehouse. Please do not return linens using any other shipping provider or any other class of shipping (i.e. Express, Next Day, Over Night these services will be billed back to your account).</p>
      <p class="note"><span class="note-title">Late Returns:</span>Our customers depend on your timely return. Please insure our items are dropped off or picked up by ParcelWing the following business day after your event. Items shipped back after the due date are considered late and will be charge a rental fee equal to 50% of your original rental rate prior to any discounts or promotions.</p>
    </section>

    <p class="closing">Should you have any questions regarding your order please contact our office at <strong>562.555.0173</strong> should you need to reach us after hours or on weekends<br>please leave a message or send an e-mail to <strong>afterhours@larkspurdraperys.example</strong></p>
  </main>
</body>
</html>
```